Pinecrest Renovations - Get the creative juices going!!

Pinecrest does not do the actual renovation work. The company provides high end project management of renovation (primarily residential - with an eye toward commercial) The renovation work could look very different between projects. This company manages the work of contractors, architects and interior designers (either subcontracted directly by Pinecrest or hired by the client and entrusted to Pinecrest to manage). Clients are high end in the economic scale and the card needs to have a high end feel to it.

The owner is female, but the audience will be heavily slanted male. It should not be a "feminine" or "masculine" looking card. If anything, slant more on the masculine side. Clean, simple, yet creative and artistically appealing. The card design should complement and in no way compete with the logo.

When people think of our company: trust, integrity, dynamic, limitless possibilities, transition, energy, creative. We plan to expand in the future to be international.

There will also be a contest running for stationary. Please check that section, as well.

***Black is 80-90 percent black. Not stark black

Tight timeline. Needs cards printed quickly!

Residential

```html
<!DOCTYPE html>
<html lang="en">
<head>
<meta charset="utf-8">
<title>Pinecrest Renovations – Business Card</title>
<link rel="stylesheet" href="https://fonts.googleapis.com/css2?family=Libre+Baskerville:ital,wght@0,400;1,400&family=Questrial&display=swap">
<style>
  :root {
    --teal: #1aa89c;
    --ink: #3b3b3b;
    --ink-soft: #454545;
    --paper: #ffffff;
  }
  html, body {
    margin: 0;
    padding: 0;
    width: 1200px;
    height: 702px;
    overflow: hidden;
    background: var(--paper);
  }
  .card {
    position: relative;
    width: 1200px;
    height: 702px;
    background: var(--paper);
    overflow: hidden;
  }
  .card-frame {
    position: absolute;
    left: 42px;
    top: 42px;
    width: 1116px;
    height: 619px;
    box-sizing: border-box;
    border: 4px solid var(--teal);
    border-radius: 46px;
  }
  .brand-mark {
    position: absolute;
    left: 222px;
    top: 328px;
    width: 56px;
    height: 56px;
    background: var(--teal);
  }
  .title-band {
    position: absolute;
    left: 622px;
    top: 63px;
    width: 48px;
    height: 581px;
    background: var(--teal);
  }
  /* Portrait layer turned to read bottom-to-top */
  .vertical-layer {
    position: absolute;
    left: 0;
    top: 702px;
    width: 702px;
    height: 1200px;
    transform-origin: 0 0;
    transform: rotate(-90deg);
  }
  .vertical-layer > * {
    position: absolute;
    margin: 0;
    white-space: nowrap;
  }
  .company-name {
    left: 57px;
    top: 362px;
    font-family: "Questrial", sans-serif;
    font-size: 41px;
    line-height: 42px;
    letter-spacing: 1.6px;
    color: var(--ink);
    text-transform: uppercase;
  }
  .person-name {
    right: 117px;
    top: 508px;
    font-family: "Libre Baskerville", serif;
    font-size: 94px;
    line-height: 100px;
    color: var(--ink);
    letter-spacing: 1px;
  }
  .person-title {
    right: 108px;
    top: 624px;
    font-family: "Libre Baskerville", serif;
    font-style: italic;
    font-size: 40px;
    line-height: 46px;
    color: var(--paper);
    letter-spacing: 1px;
  }
  .contact-line {
    right: 111px;
    font-family: "Libre Baskerville", serif;
    font-size: 46px;
    line-height: 56px;
    color: var(--ink-soft);
  }
  .contact-number  { top: 784px; }
  .contact-address { top: 860px; }
  .contact-email   { top: 938px; }
  .contact-web     { top: 1014px; }
</style>
</head>
<body>
  <main class="card">
    <div class="card-frame"></div>
    <div class="brand-mark" aria-hidden="true"></div>
    <div class="title-band"></div>
    <div class="vertical-layer">
      <p class="company-name">Pinecrest Renovations</p>
      <h1 class="person-name">NAME</h1>
      <p class="person-title">TITEL</p>
      <p class="contact-line contact-number">number</p>
      <p class="contact-line contact-address">address</p>
      <p class="contact-line contact-email">email</p>
      <p class="contact-line contact-web">web</p>
    </div>
  </main>
</body>
</html>
```